Design business cards for Ironvale Barbers (Opening March so won't need finalised till January2018

Ironvale Barbers is the new age barbers and skincare for all men. Creating tailor made haircuts & customised skincare solutions for the perfect healthy manly look. The Barbers will have a industrial, rustic, worldly feel about it. Rustic red brick wall with old wine barrels as the work stations with the old fashion barber chairs. Concrete floor and a bit corrugated iron around.
Target Market(s)
Professional males who like a great haircut, wet shave and may consider a facial if in the right environment. Total pampering experience in a boys environment.
Industry/Entity Type
Barber
Contact Information for Business Card
Front- Logo - address is 42 Kowhai Rd Taupo
Ph - (07) 548 9163
www.ironvalebarbers.com
email - hello@ironvale.co.nz
Back of card
Mens Haircare - Wet Shaving - Facials - Skin Prescriptions
We are doing a loyalty program - 6 squares numbered then 7th free
Colors
Designer to choose colors to be used in the design.
Requirements
Must have
- Clean simple easy to read.
Nice to have
- Our current colours are white font on black background but thinking we need to introduce another colour. Maybe white logo on a copper, bronze or rusty background. Or even a rustic red brick wall with white writing. Want it clean simple to read. Maybe a burgundy?
Should not have
- no images like heads, scissors, razors please

```html
<!DOCTYPE html>
<html lang="en">
<head>
<meta charset="utf-8">
<title>Ironvale Barbers – Business Card</title>
<link href="https://fonts.googleapis.com/css2?family=Roboto+Condensed:wght@700&display=swap" rel="stylesheet">
<style>
  :root {
    --page: #ffffff;
    --burgundy: #3f0003;
    --copper: #b8672b;
    --copper-light: #d9934f;
    --copper-dark: #8a4518;
    --guide: rgba(184, 103, 43, 0.45);
    --ink: #ffffff;
  }
  html, body {
    margin: 0;
    width: 1200px;
    height: 1200px;
    overflow: hidden;
    background: var(--page);
    font-family: "Roboto Condensed", "Arial Narrow", sans-serif;
    font-weight: 700;
  }
  .canvas { position: relative; width: 1200px; height: 1200px; }
  .card {
    position: absolute;
    left: 230px;
    width: 739px;
    height: 411px;
    background: var(--burgundy);
    color: var(--ink);
  }
  .card--front { top: 142px; }
  .card--back { top: 618px; }

  .guides { position: absolute; inset: 0; }

  .map-area {
    position: absolute;
    left: 258px; top: 54px;
    width: 208px; height: 300px;
    border-radius: 40% 55% 45% 50%;
    background: linear-gradient(90deg, var(--copper-dark), var(--copper-light) 45%, var(--copper) 100%);
    opacity: 0.85;
  }

  .brand-name {
    position: absolute;
    left: 0; right: 0;
    top: 176px;
    text-align: center;
    font-size: 44px;
    line-height: 1;
    letter-spacing: 1px;
    color: var(--ink);
    text-transform: uppercase;
  }

  .contact {
    position: absolute;
    top: 304px;
    font-size: 18.5px;
    line-height: 23px;
    letter-spacing: 0.4px;
  }
  .contact--left { left: 57px; }
  .contact--right { right: 58px; text-align: right; }

  .services {
    position: absolute;
    left: 81px; top: 81px;
    margin: 0; padding: 0;
    list-style: none;
  }
  .services li {
    font-size: 30px;
    line-height: 1;
    height: 67px;
    letter-spacing: 0.6px;
  }

  .appointment {
    position: absolute;
    left: 400px;
    width: 259px;
    color: var(--copper);
    font-size: 21px;
    line-height: 1;
    letter-spacing: 0.4px;
    padding-bottom: 4px;
    border-bottom: 1px solid var(--copper);
  }
  .appointment--date { top: 236px; }
  .appointment--time { top: 289px; }
</style>
</head>
<body>
<div class="canvas">

  <section class="card card--front">
    <svg class="guides" width="739" height="411" viewBox="0 0 739 411" aria-hidden="true">
      <g fill="none" stroke="var(--guide)" stroke-width="0.8">
        <rect x="40.5" y="41.5" width="657" height="328"/>
        <rect x="46.5" y="47.5" width="645" height="315"/>
        <line x1="160.5" y1="41" x2="160.5" y2="370"/>
        <line x1="369.5" y1="41" x2="369.5" y2="370"/>
        <line x1="577.5" y1="41" x2="577.5" y2="370"/>
        <line x1="40" y1="151.5" x2="698" y2="151.5"/>
        <line x1="40" y1="260.5" x2="698" y2="260.5"/>
      </g>
    </svg>

    <div class="map-area" role="img" aria-label="Copper map of New Zealand and Tasmania behind the name"></div>

    <div class="brand-name">Ironvale Barbers</div>

    <address class="contact contact--left" style="font-style:normal">
      42 Kowhai Rd Taupo<br>
      +64 27 548 9163
    </address>
    <address class="contact contact--right" style="font-style:normal">
      hello@ironvale.co.nz<br>
      www.ironvalebarbers.com
    </address>
  </section>

  <section class="card card--back">
    <ul class="services">
      <li>Men’s Haircare</li>
      <li>Wet Shaving</li>
      <li>Facials</li>
      <li>Skin Prescriptions</li>
    </ul>
    <div class="appointment appointment--date">Date</div>
    <div class="appointment appointment--time">Time</div>
  </section>

</div>
</body>
</html>
```